Ho/Lux Business Card & Stationary
BluebirdNests
@PH - We have readied the new concepts.
please let us know as soon as the new resources / logo source files are uploaded to update in our designs & upload in the contest.
Thanks
Attention Designers:
The project has been put on hold until the vector files for logo are uploaded.
#16 looks great! I notice that my picture isn't very good (glasses are tilted), so I will upload another in a couple of days, but other than that, it's great!
#15 is very good. I would like the checkmark and balloon bigger though...
I like #9 (the top left one). Can you move the checkmark down to where the balloon is and make it bigger? Can you move the balloon up and slightly closer to the centre? Back side needs a checkmark.
Nice, but balloon should be larger and watermark style, the checkmark not a watermark
#7 is pretty good, but swap locations of the checkmark and balloon
If possible, I would like the holux balloon to be like a watermark and larger
I don't want "Where in Georgetown is Owen".
The back of #1 looks good but make checkmark red and add BluebirdNests at the top like #2.
can the holux balloon go behind Bluebird nests (more on the right)? I prefer the checkmark location in the first draft.
I like, but the checmark needs to be red. Also I need the Ho/Lux baloon integrated somehow...

```html
<!DOCTYPE html>
<html lang="en">
<head>
<meta charset="utf-8">
<title>Bluebird Nests Stationery Set</title>
<link href="https://fonts.googleapis.com/css2?family=Cinzel:wght@600&family=Open+Sans:wght@400;600&display=swap" rel="stylesheet">
<style>
  :root{
    --stage:#dcdfe3;
    --paper:#ffffff;
    --paper-tint:#eef4fb;
    --blue:#1f7fd1;
    --blue-deep:#0f5ea8;
    --blue-light:#6fb3ea;
    --ink:#2f4a68;
    --muted:#6d7a88;
    --accent:#d9262c;
  }
  *{box-sizing:border-box;margin:0;padding:0}
  html,body{width:1200px;height:346px;overflow:hidden;background:var(--stage)}
  body{position:relative;font-family:"Open Sans",Arial,sans-serif;color:var(--ink)}
  .piece{position:absolute;background:var(--paper);overflow:hidden}
  .piece svg.art{position:absolute;inset:0;width:100%;height:100%}
  .brand{position:absolute;display:flex;align-items:center;gap:4px;font-family:"Cinzel",Georgia,serif;font-weight:600;color:var(--ink);white-space:nowrap;letter-spacing:.04em}
  .brand .dot{border-radius:50%;background:var(--accent);flex:none}
  .fine{position:absolute;font-size:4px;line-height:1.35;color:var(--muted);white-space:nowrap}

  /* Business card front */
  .card-front{left:24px;top:142px;width:125px;height:86px}
  .card-front .photo{position:absolute;left:6px;top:8px;width:26px;height:30px;background:linear-gradient(180deg,#c9d6e2,#8a9fb4);border:1px solid #fff}
  .card-front .brand{left:40px;top:44px;font-size:6.5px}
  .card-front .brand .dot{width:9px;height:9px}
  .card-front .name{position:absolute;left:36px;top:12px;font-size:5px;font-weight:600;color:#fff;white-space:nowrap}
  .card-front .role{position:absolute;left:36px;top:19px;font-size:4px;color:#e3f0fb;white-space:nowrap}
  .card-front .fine{left:40px;top:60px}

  /* Business card back */
  .card-back{left:24px;top:233px;width:125px;height:86px;background:var(--blue)}
  .card-back .brand{left:10px;top:12px;font-size:7px;color:#fff}
  .card-back .brand .dot{width:10px;height:10px}
  .card-back .fine{left:10px;top:64px;color:#fff;font-size:4.2px}

  /* Letterheads */
  .letterhead{top:19px;width:228px;height:307px}
  .letterhead.first{left:166px}
  .letterhead.second{left:403px}
  .letterhead .brand{left:30px;top:16px;font-size:10.5px}
  .letterhead .brand .dot{width:16px;height:16px}
  .letterhead .fine{left:24px;top:268px}

  /* Note cards */
  .notecard{left:643px;width:245px}
  .notecard.upper{top:96px;height:72px}
  .notecard.lower{top:206px;height:89px}
  .notecard .brand{left:12px;top:8px;font-size:8px}
  .notecard .brand .dot{width:12px;height:12px}
  .notecard.lower .brand{top:16px}
  .notecard .fine{left:12px;top:26px}

  /* Envelopes */
  .envelope{left:905px;width:276px}
  .envelope.back{top:96px;height:86px}
  .envelope.front{top:197px;height:101px}
  .envelope .seal{position:absolute;left:130px;top:32px;width:14px;height:14px;border-radius:50%;background:var(--accent)}
  .envelope .brand{left:106px;top:20px;font-size:7px}
  .envelope .brand .dot{width:10px;height:10px}
  .envelope .fine{left:100px;top:34px}
</style>
</head>
<body>

<!-- Business card: front -->
<div class="piece card-front">
  <svg class="art" viewBox="0 0 125 86" preserveAspectRatio="none" aria-hidden="true">
    <path d="M0 0H125V30Q60 40 0 46Z" fill="var(--blue)"/>
    <path d="M0 46Q60 40 125 30V33Q60 43 0 50Z" fill="var(--blue-light)"/>
    <path d="M0 78Q62 72 125 76V86H0Z" fill="var(--blue)"/>
  </svg>
  <div class="photo" role="img" aria-label="Portrait photo of the agent"></div>
  <div class="name">T. Owen Dalworth</div>
  <div class="role">Sales Associate</div>
  <div class="brand"><span>Bluebird Nests</span><span class="dot"></span></div>
  <div class="fine">555-0142 · tdalworth@bluebirdnests.net</div>
</div>

<!-- Business card: back -->
<div class="piece card-back">
  <svg class="art" viewBox="0 0 125 86" preserveAspectRatio="none" aria-hidden="true">
    <path d="M0 56Q62 46 125 52V86H0Z" fill="var(--blue-deep)"/>
  </svg>
  <div class="brand"><span>Bluebird Nests</span><span class="dot"></span></div>
  <div class="fine">Realtor, Bluebird Nests</div>
</div>

<!-- Letterhead: first page -->
<div class="piece letterhead first">
  <svg class="art" viewBox="0 0 228 307" preserveAspectRatio="none" aria-hidden="true">
    <defs><linearGradient id="lhTint" x1="0" y1="0" x2="0" y2="1"><stop offset="0" stop-color="var(--paper-tint)"/><stop offset="1" stop-color="#fff"/></linearGradient></defs>
    <rect width="228" height="70" fill="url(#lhTint)"/>
    <path d="M0 0H9Q3 120 14 307H0Z" fill="var(--blue)"/>
    <path d="M9 0H12Q6 120 17 307H14Q3 120 9 0Z" fill="var(--blue-light)"/>
    <path d="M0 294Q114 280 228 290V307H0Z" fill="var(--blue)"/>
  </svg>
  <div class="brand"><span>Bluebird Nests</span><span class="dot"></span></div>
  <div class="fine">12 Main Street, Georgetown · 555-0142<br>tdalworth@bluebirdnests.net</div>
</div>

<!-- Letterhead: second page -->
<div class="piece letterhead second">
  <svg class="art" viewBox="0 0 228 307" preserveAspectRatio="none" aria-hidden="true">
    <rect width="228" height="70" fill="url(#lhTint)"/>
    <path d="M0 0H9Q3 120 14 307H0Z" fill="var(--blue)"/>
    <path d="M0 294Q114 280 228 290V307H0Z" fill="var(--blue)"/>
  </svg>
  <div class="brand"><span>Bluebird Nests</span><span class="dot"></span></div>
</div>

<!-- Note card: upper -->
<div class="piece notecard upper">
  <svg class="art" viewBox="0 0 245 72" preserveAspectRatio="none" aria-hidden="true">
    <path d="M0 58Q120 50 245 56V72H0Z" fill="var(--blue)"/>
  </svg>
  <div class="brand"><span>Bluebird Nests</span><span class="dot"></span></div>
  <div class="fine">T. Owen Dalworth<br>12 Main Street</div>
</div>

<!-- Note card: lower -->
<div class="piece notecard lower">
  <svg class="art" viewBox="0 0 245 89" preserveAspectRatio="none" aria-hidden="true">
    <rect width="245" height="40" fill="url(#lhTint)"/>
    <path d="M0 0H245V6Q120 12 0 4Z" fill="var(--blue)"/>
    <path d="M0 76Q120 68 245 74V89H0Z" fill="var(--blue)"/>
  </svg>
  <div class="brand"><span>Bluebird Nests</span><span class="dot"></span></div>
</div>

<!-- Envelope: back with flap -->
<div class="piece envelope back">
  <svg class="art" viewBox="0 0 276 86" preserveAspectRatio="none" aria-hidden="true">
    <path d="M0 0H276L138 46Z" fill="var(--blue)"/>
    <path d="M0 0L138 46L276 0" fill="none" stroke="var(--blue-light)" stroke-width="2"/>
    <path d="M0 86L110 44M276 86L166 44" stroke="#d7dee6" stroke-width="1" fill="none"/>
  </svg>
  <div class="seal"></div>
</div>

<!-- Envelope: front -->
<div class="piece envelope front">
  <svg class="art" viewBox="0 0 276 101" preserveAspectRatio="none" aria-hidden="true">
    <path d="M0 0H276L138 20Z" fill="var(--blue)"/>
    <path d="M0 101L138 52L276 101" fill="none" stroke="#d7dee6" stroke-width="1"/>
  </svg>
  <div class="brand"><span>Bluebird Nests</span><span class="dot"></span></div>
  <div class="fine">12 Main Street, Georgetown</div>
</div>

</body>
</html>
```